Business Card
Larkframe, LLC
Professional
Omar Pettis
Founder and CEO
412 Birchwell Rd
Springfield, NJ 07134
omar.pettis@larkframe.com
www.larkframe.com
I am open on the font choice. A different font may be used if it works visually.
Nothing
Illustrator file of our Corporate Logo

```html
<!DOCTYPE html>
<html lang="en">
<head>
<meta charset="utf-8">
<title>Larkframe, LLC — Business Card</title>
<link rel="stylesheet" href="https://fonts.googleapis.com/css2?family=Montserrat:wght@600&family=Questrial&display=swap">
<style>
  :root {
    --backdrop: #27303b;
    --card-white: #ffffff;
    --brand-blue: #1c6db4;
    --brand-blue-deep: #0b4a8c;
    --brand-green: #6cb52e;
    --tagline-grey: #6f7780;
    --text-on-blue: #ffffff;
    --text-soft: #d6e6f5;
  }
  * { margin: 0; padding: 0; box-sizing: border-box; }
  html, body { width: 1200px; height: 901px; overflow: hidden; }
  body {
    background: var(--backdrop);
    font-family: "Questrial", "Century Gothic", sans-serif;
    position: relative;
  }
  .card {
    position: absolute;
    left: 250px;
    width: 700px;
    height: 400px;
    border-radius: 22px;
    overflow: hidden;
    background: var(--card-white);
  }
  .card--front { top: 40px; }
  .card--back { top: 470px; }

  .logo { display: flex; align-items: center; gap: 18px; }
  .logo__dot {
    width: 74px; height: 74px; border-radius: 50%;
    background: var(--brand-blue);
    flex: none;
  }
  .logo__name {
    font-family: "Montserrat", sans-serif;
    font-weight: 600;
    font-size: 54px;
    color: var(--brand-blue);
    line-height: 1;
    letter-spacing: -0.5px;
    white-space: nowrap;
  }
  .logo__tagline {
    font-size: 17px;
    color: var(--tagline-grey);
    margin-top: 6px;
    letter-spacing: 0.3px;
    white-space: nowrap;
  }
  .card--front .logo {
    position: absolute; left: 50%; top: 50%;
    transform: translate(-50%, -50%);
  }

  .card--back .logo {
    position: absolute; left: 200px; top: 48px;
  }
  .card--back .logo__dot { width: 64px; height: 64px; }
  .card--back .logo__name { font-size: 46px; }
  .card--back .logo__tagline { font-size: 15px; }

  .accent-line {
    position: absolute; left: 0; right: 0; top: 176px;
    height: 5px; background: var(--brand-green);
  }
  .contact-band {
    position: absolute; left: 0; right: 0; top: 181px; bottom: 0;
    background: linear-gradient(160deg, var(--brand-blue) 0%, var(--brand-blue-deep) 100%);
    color: var(--text-on-blue);
  }
  .person { position: absolute; left: 44px; top: 30px; }
  .person__name { font-size: 22px; }
  .person__title { font-size: 15px; color: var(--text-soft); margin-top: 4px; }
  .details {
    position: absolute; left: 360px; top: 30px;
    font-size: 16px; line-height: 1.5; list-style: none;
  }
  .website {
    position: absolute; right: 40px; bottom: 26px;
    font-size: 20px; letter-spacing: 0.4px;
  }
</style>
</head>
<body>
  <section class="card card--front" aria-label="Card front">
    <div class="logo">
      <span class="logo__dot"></span>
      <div>
        <div class="logo__name">Larkframe</div>
        <div class="logo__tagline">Frame Stories • Grow Audiences</div>
      </div>
    </div>
  </section>

  <section class="card card--back" aria-label="Card back">
    <div class="logo">
      <span class="logo__dot"></span>
      <div>
        <div class="logo__name">Larkframe</div>
        <div class="logo__tagline">Frame Stories • Grow Audiences</div>
      </div>
    </div>
    <div class="accent-line"></div>
    <div class="contact-band">
      <div class="person">
        <div class="person__name">Omar Pettis</div>
        <div class="person__title">Founder and CEO</div>
      </div>
      <ul class="details">
        <li>412 Birchwell Rd</li>
        <li>Springfield, NJ 07134</li>
        <li>P: 908-555-0147</li>
        <li>E: omar.pettis@larkframe.com</li>
      </ul>
      <div class="website">www.larkframe.com</div>
    </div>
  </section>
</body>
</html>
```